Web Design Project

We are an IT System Integrator. We provide Norvik 500 ERP System, CRM etc. We also provide hardware, networking servicing. Please look at www.brinquot.com.sg. They provide the same service as us. We like to redesign our web site. I will attached the color that I prefer for reference.

Our website is www.ravdu.com.sg.  It has been created about 14 years ago.  We are trying to revamp it with a new look and information.   The new website must be informative, fast.    I have attached an attachment which show the color that I prefer(brownish golden).   

Our competitor (www.brinquot.com) is carrying the same trade as us.  They have all the informations In their website that we will like to have.  Therefore I recommend you to take a look at my competitor website and have a better   
understanding on the kind of information I would like to have for my new website.

This project is guarantee to the person with the best design.  We can have it guarantee.

Target Market(s)

Corporate and companies

Industry/Entity Type

Hardware

```html
<!DOCTYPE html>
<html lang="en">
<head>
<meta charset="utf-8">
<title>Ravdu Information System</title>
<link rel="stylesheet" href="https://fonts.googleapis.com/css2?family=Open+Sans:wght@300;400;600;700&family=Noto+Serif:ital@1&display=swap">
<style>
:root{
  --brown:#8e6d3a;
  --brown-dark:#6e5228;
  --gold-light:#e9d8ad;
  --gold:#c49a52;
  --band:#eeebe4;
  --nav-text:#5b5146;
  --body-text:#666;
  --title-text:#777;
  --panel:#efefef;
  --footer:#3d3d3d;
  --footer-text:#c8c8c8;
}
*{margin:0;padding:0;box-sizing:border-box}
html,body{width:1099px;height:1200px;overflow:hidden;background:#fff}
body{font-family:"Open Sans",Arial,sans-serif}
.page{position:relative;width:1020px;height:1114px;transform:scale(1.0775);transform-origin:0 0}
.topbar{position:absolute;left:0;top:0;width:1020px;height:50px;background:var(--brown)}
.utility{position:absolute;right:29px;top:17px;display:flex;gap:14px;list-style:none;font-size:11px;color:#fff}
.utility li::before{content:"";display:inline-block;width:4px;height:4px;border-radius:50%;background:#fff;margin-right:7px;vertical-align:middle}
.navband{position:absolute;left:0;top:50px;width:1020px;height:100px;background:var(--band);border-top:2px solid #fff;box-shadow:inset 0 -3px 4px rgba(0,0,0,.12)}
.heroband{position:absolute;left:0;top:150px;width:1020px;height:230px;background:var(--brown)}
.brand{position:absolute;left:30px;top:12px;width:282px;height:196px}
.brand svg{position:absolute;left:0;top:0}
.brand-name{position:absolute;left:0;top:90px;width:282px;display:flex;align-items:center;justify-content:center;gap:8px;font-size:16px;font-weight:600;color:#3a2c14}
.brand-name i{display:block;width:14px;height:14px;border-radius:50%;background:#3a2c14}
.mainnav{position:absolute;right:29px;top:88px;display:flex;align-items:center;gap:0;list-style:none;font-size:13px;font-weight:700;color:var(--nav-text)}
.mainnav li{margin-left:22px;display:flex;align-items:center;height:27px}
.mainnav li.has-menu::after{content:"";margin-left:8px;border-left:4px solid transparent;border-right:4px solid transparent;border-top:5px solid #3a3128}
.mainnav li.current{background:linear-gradient(#c39c5b,#8c6a33);color:#fff;padding:0 10px;border-radius:3px;box-shadow:0 2px 3px rgba(0,0,0,.35)}
.slider{position:absolute;left:30px;top:180px;width:961px;height:390px}
.slider svg.frame{position:absolute;left:0;top:0}
.slide-photo{position:absolute;left:15px;top:12px;width:932px;height:334px;background:linear-gradient(90deg,#f1f1f0 0%,#e9e4e0 30%,#dfe9f0 55%,#9fc3dc 75%,#eef2f4 100%);border:1px solid #ddd}
.caption{position:absolute;left:547px;top:184px;width:400px;height:120px;background:rgba(40,42,44,.88);color:#fff;padding:22px 26px}
.caption h2{font-size:14px;font-weight:700;margin-bottom:6px}
.caption p{font-size:12.5px;line-height:21px}
.arrow{position:absolute;top:228px;width:36px;height:99px;background:#4c4c4c;display:flex;align-items:center;justify-content:center}
.arrow.prev{left:18px}.arrow.next{left:967px}
.dots{position:absolute;left:451px;top:538px;display:flex;gap:10px}
.dots span{width:16px;height:16px;border-radius:50%;background:radial-gradient(circle at 50% 35%,#fafafa,#cfcfcf);box-shadow:0 1px 2px rgba(0,0,0,.3)}
.dots span.active{background:radial-gradient(circle at 50% 35%,#d2a547,#8a6315)}
.content{position:absolute;left:35px;top:604px;width:628px;color:var(--body-text)}
.content h1{font-size:26px;font-weight:300;color:var(--title-text);margin-bottom:16px}
.content p{font-size:12.6px;line-height:18px;margin-bottom:18px}
.testimonials{position:absolute;left:714px;top:656px;width:262px;height:242px;background:var(--panel);border:1px solid #d6d6d6;border-radius:5px;box-shadow:inset 0 0 0 2px #fff}
.testimonials h3{height:46px;border-bottom:1px solid #ddd;box-shadow:0 1px 0 #fff;padding:14px 16px;font-size:15px;font-weight:400;color:#2e2a22}
.testimonials h4{margin:18px 17px 14px;font-size:13px;font-weight:700;color:#444}
.quote{position:relative;margin:0 40px 0 56px;font-family:"Noto Serif",Georgia,serif;font-style:italic;font-size:12.5px;line-height:20px;color:#777}
.quote .mark{position:absolute;font-family:Georgia,serif;font-style:normal;font-size:52px;color:#bbb;line-height:1}
.quote .open{left:-40px;top:-10px}
.quote .close{right:-28px;top:30px}
.footer{position:absolute;left:0;top:1034px;width:1020px;height:80px;background:var(--footer);color:var(--footer-text);font-size:11px}
.footer ul{position:absolute;left:29px;top:13px;display:flex;gap:12px;list-style:none}
.footer .copy{position:absolute;right:29px;top:13px}
</style>
</head>
<body>
<div class="page">
  <header>
    <div class="topbar">
      <ul class="utility"><li>FAQs</li><li>Resources</li><li>Contact Us</li></ul>
    </div>
    <div class="navband"></div>
    <div class="heroband"></div>
    <div class="brand">
      <svg width="282" height="196" viewBox="0 0 282 196">
        <defs>
          <linearGradient id="badgeFill" x1="0" y1="0" x2="1" y2="1">
            <stop offset="0" stop-color="#b7893d"/>
            <stop offset=".45" stop-color="#f3e5c0"/>
            <stop offset="1" stop-color="#c8a060"/>
          </linearGradient>
        </defs>
        <path d="M1 1 H281 V168 Q210 178 141 194 Q72 178 1 168 Z" fill="url(#badgeFill)" stroke="#9a7a44" stroke-width="1.5"/>
      </svg>
      <div class="brand-name"><i></i>Ravdu Information System</div>
    </div>
    <ul class="mainnav">
      <li class="current">Home</li>
      <li class="has-menu">Solutions</li>
      <li class="has-menu">Hardware</li>
      <li class="has-menu">Services</li>
      <li class="has-menu">Clients</li>
      <li class="has-menu">About Us</li>
      <li>Contact</li>
    </ul>
  </header>

  <section class="slider">
    <svg class="frame" width="961" height="390" viewBox="0 0 961 390">
      <path d="M10 0 H951 Q961 0 961 10 V352 Q961 362 940 366 Q700 392 480 388 Q260 392 20 366 Q0 362 0 352 V10 Q0 0 10 0 Z" fill="#fff" stroke="#ddd"/>
    </svg>
    <div class="slide-photo" role="img" aria-label="Photo of a smiling customer support agent wearing a headset"></div>
    <div class="caption">
      <h2>Lorem Ipsum Dolor</h2>
      <p>Sea cu solet suavitate, et solum placerat vix. Te pro alienum sadipscing ullamcorper, summo exerci appetere</p>
    </div>
  </section>
  <div class="arrow prev"><svg width="12" height="20"><path d="M10 2 L3 10 L10 18" fill="none" stroke="#aaa" stroke-width="2"/></svg></div>
  <div class="arrow next"><svg width="12" height="20"><path d="M2 2 L9 10 L2 18" fill="none" stroke="#aaa" stroke-width="2"/></svg></div>
  <div class="dots"><span></span><span class="active"></span><span></span><span></span><span></span></div>

  <main class="content">
    <h1>Main Title Goes Here</h1>
    <p>Lorem ipsum dolor sit amet, his laoreet theophrastus ut, id eum sententiae persequeris, diceret inimicus scriptorem cu nec. Te quo utroque albucius constituam, mei et duis iracundia, at est probo decore aperiri. Aperiam meliore molestie ei eos, facer nullam per ad, no sanctus pericula vix. Ea aeque mucius offendit sea, justo alterum pro ut, at percipit accommodare vel.</p>
    <p>Sea cu solet suavitate, et solum placerat vix. Te pro alienum sadipscing ullamcorper, summo exerci appetere ne usu, pro ei diam aliquip meliore. Ad nostrud reprimique mea, integre elaboraret referrentur ius cu. Graece iisque sententiae an vel. Alia possit ut qui, erroribus suscipiantur ea eam.</p>
    <p>Tibique corpora senserit pro ad, delicata disputationi sea ex. In modus voluptatibus pri, nam eu liber causae sapientem. Everti maluisset cu vis, usu harum tempor maluisset ut, laoreet nonumes ex pro. Ut stet altera melius sea. Mei no dicant facilis abhorreant, ne esse veniam verterem pro. Alii velit nonumes usu ad. Et tation adipiscing definitiones quo.</p>
  </main>

  <aside class="testimonials">
    <h3>Testimonials</h3>
    <h4>Lorem ipsum dolor sit amet</h4>
    <p class="quote"><span class="mark open">&ldquo;</span>Sea cu solet suavitate, et solum placerat vix. Te pro alienum sadipscing<span class="mark close">&rdquo;</span></p>
  </aside>

  <footer class="footer">
    <ul><li>Home</li><li>Terms &amp; Conditions</li><li>Privacy Policy</li><li>Sitemap</li></ul>
    <div class="copy">&copy; 2013 Ravdu Information System. All rights reserved.</div>
  </footer>
</div>
</body>
</html>
```